Northern Summit Builders & Affiliates Redesigning our Look

We need stationary (letterhead, envelopes, notepads, invoicing templates, etc) that all coordinate. We are an commerial and residential exteriors construction company that operates 3 companies which all run exclusively, however, the compliment one another well.

Northern Summit Builders (this company installs exteriors on jobsites both residential and commercial)
Northern Summit Roofing & Building Supply (this company sells exterior building materials to homeowners and builders.)
Northern Summit Dumpster Services (This company delivers roll away dumpster cans to homeowners and builders)

Just a note: When I say we do exterior work. We do roofing, siding, stone, windows/doors, gutters, and decks.

We are looking for stationary that includes all three and keeps with our patriotic theme

Info on our firm:
Address: 2718 Tamarind Rd, Elkton MI 48512
Phone: 231-555-0172
Website: www.northernsummit-example.us

Target Market(s)

Our companies target market is vast. We work in the B2B space as well as with homeowner (retail customers). We are in the home and commercial buiding construction field. We specialized in exteriors. (Roofing, Siding, Stone, Windows, Doors, Decks, Gutters)

Industry/Entity Type

Construction

Colors
ec1f27
ffffff
0555a3

Requirements
Must have
• Would like to have a clean professional look with a patriotic theme
Nice to have
• Red/White/Blue

```html
<!DOCTYPE html>
<html lang="en">
<head>
<meta charset="utf-8">
<title>Northern Summit Stationery Set</title>
<link href="https://fonts.googleapis.com/css2?family=Source+Sans+3:wght@400;700&family=Source+Serif+4:wght@400;700&display=swap" rel="stylesheet">
<style>
  :root{
    --red:#ec1f27;
    --blue:#0555a3;
    --edge:#1f3fe0;
    --white:#ffffff;
    --ink:#111111;
    --shadow:#b9b9b9;
    --rule:#9fb3ad;
    --purple:#5b2d8e;
    --olive:#8a9a5b;
    --sans:"Source Sans 3", Arial, sans-serif;
    --serif:"Source Serif 4", Georgia, serif;
  }
  *{box-sizing:border-box;margin:0;padding:0}
  html,body{width:1200px;height:1200px;overflow:hidden;background:var(--white)}
  body{position:relative;font-family:var(--sans);color:var(--ink)}
  .sheet{position:absolute;background:var(--white);border:2px solid var(--edge);box-shadow:9px 9px 0 var(--shadow);overflow:hidden}
  .wave{position:absolute;inset:0;width:100%;height:100%}
  .brand{position:absolute;font-family:var(--sans);font-weight:700;color:var(--ink);line-height:1.05;white-space:nowrap}
  .brand .name{display:block}
  .contact{position:absolute;color:var(--edge);font-size:7px;line-height:1.35;font-style:normal;white-space:nowrap}

  .letterhead{left:32px;top:148px;width:442px;height:568px}
  .letterhead .brand{left:30px;top:26px;font-size:17px}
  .letterhead .contact,.invoice .contact{left:318px;top:500px;font-size:6.5px}

  .notepad{left:425px;top:213px;width:233px;height:347px}
  .notepad .brand{left:14px;top:12px;font-size:8px}
  .notepad .contact{right:9px;top:10px;text-align:center;font-size:4.6px}
  .notepad .contact strong{display:block;font-size:7.5px}

  .invoice{left:692px;top:144px;width:442px;height:570px}
  .invoice .brand{left:30px;top:26px;font-size:17px}
  .inv-title{position:absolute;right:26px;top:82px;font-size:20px;color:var(--purple);text-align:right;line-height:1}
  .inv-date{position:absolute;right:26px;top:110px;font-size:7px;color:var(--olive)}
  .field{position:absolute;font-family:var(--serif);font-size:5px;font-weight:700}
  table{position:absolute;border-collapse:collapse;font-family:var(--serif);font-size:5px}
  td,th{border:0.6px solid var(--rule);height:12px}
  th{font-weight:700;height:11px;background:#f5f7f6}
  .t-head{left:76px;top:216px;width:342px}
  .t-items{left:76px;top:259px;width:342px}
  .t-sum{left:289px;top:414px;width:129px}
  .t-sum td:first-child{text-align:right;padding-right:2px;font-weight:700;width:84px}

  .envelope{left:342px;top:784px;width:482px;height:210px}
  .envelope .brand{left:70px;top:16px;font-size:12px}
  .flap{position:absolute;left:342px;top:696px;width:482px;height:90px}
  .flap-text{position:absolute;left:342px;top:728px;width:482px;text-align:center;font-size:7px;line-height:1.3;color:#3a0a0a;transform:rotate(180deg)}

  .card{left:859px;top:800px;width:248px;height:144px}
  .card .brand{left:22px;top:16px;font-size:8px}
  .card-phone{position:absolute;right:12px;top:6px;font-size:16px;font-weight:700;color:var(--edge);white-space:nowrap}
  .card-name{position:absolute;right:32px;top:58px;font-size:21px;font-weight:700;color:var(--edge);white-space:nowrap}
  .card-role{position:absolute;right:34px;top:82px;font-size:10px;font-weight:700;color:var(--red)}
  .card .contact{right:9px;top:104px;text-align:right;font-size:6.5px}
  .card .contact strong{font-size:7px}
</style>
</head>
<body>
<svg width="0" height="0" style="position:absolute" aria-hidden="true">
  <defs>
    <linearGradient id="flagTone" x1="0" y1="0" x2="0.4" y2="1">
      <stop offset="0" stop-color="#0555a3"/>
      <stop offset="0.33" stop-color="#2f6fe0"/>
      <stop offset="0.45" stop-color="#ec1f27"/>
      <stop offset="0.7" stop-color="#f3a4ac"/>
      <stop offset="1" stop-color="#ec1f27"/>
    </linearGradient>
  </defs>
</svg>

<section class="sheet letterhead">
  <svg class="wave" viewBox="0 0 442 568" preserveAspectRatio="none" role="img" aria-label="Waving flag ribbon decoration in blue and red">
    <path d="M0,70 C50,90 68,170 56,240 C46,300 40,380 100,450 C170,520 300,545 442,556 L442,568 L0,568 Z" fill="url(#flagTone)"/>
  </svg>
  <div class="brand"><span class="name">Northern Summit</span><span class="name">Roofing &amp; Building Supply</span></div>
  <address class="contact">2718 Tamarind Rd<br>Elkton, MI 48512<br>Phone: 231-555-0172<br>Website: www.northernsummit-example.us</address>
</section>

<section class="sheet notepad">
  <svg class="wave" viewBox="0 0 233 347" preserveAspectRatio="none" role="img" aria-label="Waving flag ribbon decoration in blue and red">
    <path d="M0,58 C30,70 36,110 22,160 C10,210 18,260 60,300 C110,330 170,338 233,340 L233,347 L0,347 Z" fill="url(#flagTone)"/>
  </svg>
  <div class="brand"><span class="name">Northern Summit</span><span class="name">Roofing &amp; Building Supply</span></div>
  <address class="contact"><strong>(231)555-0172</strong>2718 Tamarind Rd<br>Elkton, MI 48512<br>Phone: 231-555-0172<br>Website: www.northernsummit-example.us</address>
</section>

<section class="sheet invoice">
  <svg class="wave" viewBox="0 0 442 570" preserveAspectRatio="none" role="img" aria-label="Waving flag ribbon decoration in blue and red">
    <path d="M0,62 C50,84 66,170 54,240 C44,300 40,380 100,450 C170,520 300,548 442,558 L442,570 L0,570 Z" fill="url(#flagTone)"/>
  </svg>
  <div class="brand"><span class="name">Northern Summit</span><span class="name">Roofing &amp; Building Supply</span></div>
  <div class="inv-title">Invoice</div>
  <div class="inv-date">[Insert Date]</div>
  <div class="field" style="left:78px;top:145px">Invoice No.</div>
  <div class="field" style="left:250px;top:145px">Bill To:</div>
  <div class="field" style="left:334px;top:145px">Ship To:</div>
  <div class="field" style="left:78px;top:171px">Customer ID:</div>
  <table class="t-head">
    <tr><th>Date</th><th>Order No.</th><th>Sales Rep.</th><th>FOB</th><th>Ship Via</th><th>Terms</th><th>Tax ID</th></tr>
    <tr><td></td><td></td><td></td><td></td><td></td><td></td><td></td></tr>
  </table>
  <table class="t-items">
    <tr><th>Quantity</th><th>Item</th><th>Description</th><th>Discount</th><th>Taxable</th><th>Unit Price</th><th>Total</th></tr>
    <tr><td></td><td></td><td></td><td></td><td></td><td></td><td></td></tr>
    <tr><td></td><td></td><td></td><td></td><td></td><td></td><td></td></tr>
    <tr><td></td><td></td><td></td><td></td><td></td><td></td><td></td></tr>
    <tr><td></td><td></td><td></td><td></td><td></td><td></td><td></td></tr>
    <tr><td></td><td></td><td></td><td></td><td></td><td></td><td></td></tr>
    <tr><td></td><td></td><td></td><td></td><td></td><td></td><td></td></tr>
    <tr><td></td><td></td><td></td><td></td><td></td><td></td><td></td></tr>
    <tr><td></td><td></td><td></td><td></td><td></td><td></td><td></td></tr>
    <tr><td></td><td></td><td></td><td></td><td></td><td></td><td></td></tr>
    <tr><td></td><td></td><td></td><td></td><td></td><td></td><td></td></tr>
    <tr><td></td><td></td><td></td><td></td><td></td><td></td><td></td></tr>
  </table>
  <table class="t-sum">
    <tr><td>Subtotal:</td><td></td></tr>
    <tr><td>Tax:</td><td></td></tr>
    <tr><td>Shipping:</td><td></td></tr>
    <tr><td>Miscellaneous:</td><td></td></tr>
    <tr><td>Balance Due:</td><td></td></tr>
  </table>
  <address class="contact">2718 Tamarind Rd<br>Elkton, MI 48512<br>Phone: 231-555-0172<br>Website: www.northernsummit-example.us</address>
</section>

<svg class="flap" viewBox="0 0 482 90" preserveAspectRatio="none" aria-hidden="true">
  <path d="M0,90 L200,12 Q241,-4 282,12 L482,90 Z" fill="var(--red)" stroke="var(--edge)" stroke-width="1"/>
</svg>
<div class="flap-text">2718 Tamarind Rd<br>Elkton, MI 48512<br>Phone: 231-555-0172<br>Website: www.northernsummit-example.us</div>

<section class="sheet envelope">
  <svg class="wave" viewBox="0 0 482 210" preserveAspectRatio="none" role="img" aria-label="Waving flag ribbon decoration in blue and red">
    <path d="M0,0 L58,0 C40,40 30,90 48,130 C60,170 70,190 82,210 L0,210 Z" fill="url(#flagTone)"/>
  </svg>
  <div class="brand"><span class="name">Northern Summit</span><span class="name">Roofing &amp; Building Supply</span></div>
</section>

<section class="sheet card">
  <svg class="wave" viewBox="0 0 248 144" preserveAspectRatio="none" role="img" aria-label="Waving flag ribbon decoration in blue and red">
    <path d="M0,40 C14,48 16,66 12,86 C8,108 20,125 50,134 C80,140 100,142 112,144 L0,144 Z" fill="url(#flagTone)"/>
  </svg>
  <div class="brand"><span class="name">Northern Summit</span><span class="name">Roofing &amp; Building Supply</span></div>
  <div class="card-phone">231-555-0172</div>
  <div class="card-name">Dale Whitford</div>
  <div class="card-role">President</div>
  <address class="contact">2718 Tamarind Rd<br>Elkton, MI 48512<br><strong>Website: www.northernsummit-example.us</strong></address>
</section>
</body>
</html>
```